Conflict prevention NGO needs business cards ASAP

We are a small NGO based in New Caledonia working on conflict prevention, and will be attending a OGA-sponsored conference on small arms next month. Our work involves campaigning against the proliferation of small arms in this post-conflict South Pacific island, and we need business cards to match that purpose.
Our three basic guidelines are the following:
1. We would like the logo of our organisation (see attached) included on this card. We are open to a redesign of this logo to something more stylised or abstract.
2. The card would need to be double-sided: one side in French, the other in English. The text should ideally be minimalist, uncluttered, clear and concise. We prefer the card to visually communicate our mission. As such, we would like the card to present a central image or logo, which would give us the option of printing a texture onto that image/logo later.
3. I have attached images which might inspire the designer (bullets and the famous knotted gun statue). However, these are NOT prescriptive; they are simply thematic ideas, and designers should use their own creative license. We only ask that the overall business card communicate professionalism and a seriousness of purpose, rather than sentimentalism or idealism.
Thanks to everyone who is willing to offer up a design idea! I am grateful for your time, and look forward to viewing your ideas. I apologise, but this has to be a rush job. Please get in touch if you need further guidance.
Please note that our new website will go live on Wednesday evening (Brisbane time), in case it can provide inspiration: http://www.portlumineux.org/
ENGLISH SIDE
[Name, Position] Kieran Vasko, Director
[Organisation] The Centre for a Bright Harbour
[Sub-Title] The first New Caledonian think tank
[Tel] +61407913222
[Email] centreportlumineux@postvale.net
[Website] http://www.portlumineux.org/
FRENCH SIDE
[Name, Position] Kieran Vasko, Directeur
[Organisation] Le Centre pour le Port Lumineux
[Sub-Title] Le premier pôle de réflexion calédonien
[Tel] +61407913222
*Note: We are flexible on the exact way you present the above information, and you may wish to use icons instead of "Tel." for example.

```html
<!DOCTYPE html>
<html lang="en">
<head>
<meta charset="utf-8">
<title>Business cards – The Centre for a Bright Harbour</title>
<link rel="stylesheet" href="https://fonts.googleapis.com/css2?family=Roboto+Condensed:wght@400;700&display=swap">
<style>
  :root {
    --backdrop: #ebebeb;
    --card-white: #ffffff;
    --card-cream: #f8f3bd;
    --ink-blue: #1f4fa0;
    --ink-red: #d7261e;
    --ink-green: #3f9b2c;
    --mark-blue: #1f63b5;
    --photo-dark: #1c1210;
    --photo-warm: #6a4a1e;
    --foliage-dark: #1f4a14;
    --foliage-light: #5f9a2c;
  }
  * { box-sizing: border-box; margin: 0; padding: 0; }
  html, body { width: 1200px; height: 972px; overflow: hidden; }
  body {
    background: var(--backdrop);
    font-family: "Roboto Condensed", "Arial Narrow", sans-serif;
    position: relative;
  }
  .card {
    position: absolute;
    left: 300px;
    width: 600px;
    height: 344px;
    display: flex;
    box-shadow: 0 2px 8px rgba(0,0,0,0.12);
    overflow: hidden;
  }
  .card--french { top: 92px; background: var(--card-white); }
  .card--english { top: 536px; background: var(--card-cream); }

  .card__imagery { width: 270px; height: 100%; display: flex; flex-direction: column; }
  .imagery__upper {
    flex: 0 0 44%;
    background: linear-gradient(100deg, var(--photo-dark) 0%, #3a2614 45%, var(--photo-warm) 75%, #7a1d17 100%);
  }
  .imagery__lower {
    flex: 1;
    background: radial-gradient(ellipse at 55% 50%, #7d8579 0%, #6f7a5e 22%, var(--foliage-light) 45%, var(--foliage-dark) 100%);
  }

  .card__details { flex: 1; padding: 30px 0 0 30px; }
  .org-name {
    display: flex; align-items: center; gap: 10px;
    color: var(--ink-blue); font-size: 18px; font-weight: 700;
    height: 76px; margin-bottom: 14px;
  }
  .org-name__square { width: 30px; height: 30px; background: var(--mark-blue); flex: none; }
  .holder { color: var(--ink-blue); font-size: 19px; line-height: 1.2; }
  .holder__name { font-weight: 700; }
  .holder__divider { margin: 0 6px; }
  .organisation { color: var(--ink-blue); font-size: 18px; line-height: 1.2; margin-bottom: 18px; }
  .tagline { color: var(--ink-red); font-size: 18px; margin-bottom: 8px; }
  .contacts { list-style: none; }
  .contacts li {
    display: flex; align-items: center; gap: 10px;
    color: var(--ink-green); font-size: 17px; line-height: 1; margin-bottom: 9px;
  }
  .contacts svg { width: 17px; height: 17px; flex: none; }
</style>
</head>
<body>

<section class="card card--french" lang="fr">
  <div class="card__imagery">
    <div class="imagery__upper" role="img" aria-label="Photo de munitions sur fond sombre"></div>
    <div class="imagery__lower" role="img" aria-label="Photo d'une sculpture en métal devant un feuillage vert"></div>
  </div>
  <div class="card__details">
    <p class="org-name"><span class="org-name__square" aria-hidden="true"></span>Port Lumineux</p>
    <p class="holder"><span class="holder__name">Kieran Vasko</span><span class="holder__divider">|</span><span>Directeur</span></p>
    <p class="organisation">Le Centre pour le Port Lumineux</p>
    <p class="tagline">Le premier pôle de réflexion calédonien</p>
    <ul class="contacts">
      <li><svg viewBox="0 0 20 20"><circle cx="10" cy="10" r="10" fill="#3f9b2c"/><path d="M7 5.5l2 2-1 1.3c.7 1.4 1.8 2.5 3.2 3.2l1.3-1 2 2-1.2 1.5C9.8 14 6 10.2 5.5 6.7z" fill="#fff"/></svg>+61407913222</li>
      <li><svg viewBox="0 0 20 20"><circle cx="10" cy="10" r="10" fill="#3f9b2c"/><rect x="5" y="6.5" width="10" height="7" fill="#fff"/><path d="M5 6.5l5 4 5-4" stroke="#3f9b2c" fill="none"/></svg>centreportlumineux@postvale.net</li>
      <li><svg viewBox="0 0 20 20"><circle cx="10" cy="10" r="10" fill="#3f9b2c"/><g stroke="#fff" fill="none" stroke-width="1.2"><circle cx="10" cy="10" r="5.5"/><ellipse cx="10" cy="10" rx="2.3" ry="5.5"/><path d="M4.5 10h11"/></g></svg>www.portlumineux.org</li>
    </ul>
  </div>
</section>

<section class="card card--english" lang="en">
  <div class="card__imagery">
    <div class="imagery__upper" role="img" aria-label="Photo of ammunition on a dark background"></div>
    <div class="imagery__lower" role="img" aria-label="Photo of a metal sculpture in front of green foliage"></div>
  </div>
  <div class="card__details">
    <p class="org-name"><span class="org-name__square" aria-hidden="true"></span>Bright Harbour</p>
    <p class="holder"><span class="holder__name">Kieran Vasko</span><span class="holder__divider">|</span><span>Director</span></p>
    <p class="organisation">The Centre for a Bright Harbour</p>
    <p class="tagline">The first New Caledonian think tank</p>
    <ul class="contacts">
      <li><svg viewBox="0 0 20 20"><circle cx="10" cy="10" r="10" fill="#3f9b2c"/><path d="M7 5.5l2 2-1 1.3c.7 1.4 1.8 2.5 3.2 3.2l1.3-1 2 2-1.2 1.5C9.8 14 6 10.2 5.5 6.7z" fill="#fff"/></svg>+61407913222</li>
      <li><svg viewBox="0 0 20 20"><circle cx="10" cy="10" r="10" fill="#3f9b2c"/><rect x="5" y="6.5" width="10" height="7" fill="#fff"/><path d="M5 6.5l5 4 5-4" stroke="#3f9b2c" fill="none"/></svg>centreportlumineux@postvale.net</li>
      <li><svg viewBox="0 0 20 20"><circle cx="10" cy="10" r="10" fill="#3f9b2c"/><g stroke="#fff" fill="none" stroke-width="1.2"><circle cx="10" cy="10" r="5.5"/><ellipse cx="10" cy="10" rx="2.3" ry="5.5"/><path d="M4.5 10h11"/></g></svg>www.portlumineux.org</li>
    </ul>
  </div>
</section>

</body>
</html>
```